Beekeeper needs box/label design for honey/CBD and other honey-related products

We need a box (or label) design for a beekeeping company in Virginia called Larkmoor Hollow Farm. Our products will include honey mixed with CBD oil and other essential oils (vanilla, lavender, etc).The box design should be scalable to include several different honey/oil products. We would like to incorporate our current farm logo into the design. Here is a link to a honey producing company with a series of products using their honey mixed with certain oils. It's a good reference of what type box/label design we would like (https://pipandwrenly.co/pages/honey).

Target Market(s)

Retail stores and consumers

Requirements
Must have
• Larkmoor Hollow Farm name and logo

```html
<!DOCTYPE html>
<html lang="en">
<head>
<meta charset="utf-8">
<title>Larkmoor Hollow Farm – Raw Honey Label</title>
<link href="https://fonts.googleapis.com/css2?family=Cinzel:wght@400;500;600;700&display=swap" rel="stylesheet">
<style>
  :root {
    --backdrop: #1c1c1c;
    --label: #ffffff;
    --olive: #6b6a22;
    --olive-light: #9a9a3a;
    --ink: #2a2a2a;
    --watermark: #dcdccb;
    --panel-dark: #333333;
    --serif: "Cinzel", "Trajan Pro", Georgia, serif;
  }
  * { box-sizing: border-box; margin: 0; padding: 0; }
  html, body {
    width: 827px; height: 1200px; overflow: hidden;
    background: var(--backdrop);
    font-family: var(--serif);
  }
  .sheet {
    position: relative; width: 827px; height: 1200px;
    display: flex; justify-content: center; align-items: center; gap: 26px;
  }
  .label {
    position: relative; width: 380px; height: 548px;
    background: var(--label); overflow: hidden;
  }
  .flavor-initial {
    position: absolute; left: 140px; top: -78px;
    font-size: 390px; line-height: 1; font-weight: 400;
    color: var(--watermark);
  }
  /* Front */
  .brand-square {
    position: absolute; left: 46px; top: 38px; width: 100px; height: 100px;
    background: var(--olive);
  }
  .brand-name {
    position: absolute; left: 46px; top: 158px;
    color: var(--olive); font-weight: 500; line-height: 1;
  }
  .brand-name .primary { display: block; font-size: 37px; }
  .brand-name .secondary { display: block; font-size: 12px; letter-spacing: 4.5px; margin-top: 9px; }
  .product-name {
    position: absolute; left: 48px; top: 244px;
    color: var(--olive); font-size: 41px; font-weight: 600; line-height: 42px;
  }
  .rule { position: absolute; background: var(--olive); }
  .rule.product { left: 46px; top: 332px; width: 290px; height: 3px; }
  .rule.weight { left: 33px; top: 427px; width: 315px; height: 2px; }
  .infusion {
    position: absolute; left: 46px; top: 337px;
    color: var(--ink); font-size: 26px; font-weight: 500; white-space: nowrap;
  }
  .net-weight {
    position: absolute; left: 0; right: 0; top: 405px; text-align: center;
    color: var(--olive); font-size: 14px; font-weight: 500;
  }
  .front-copy {
    position: absolute; left: 33px; width: 315px; top: 433px;
    text-align: center; color: var(--ink); font-size: 11.4px; line-height: 13.4px;
  }
  /* Back */
  .back-copy {
    position: absolute; left: 38px; top: 63px; width: 308px;
    text-align: justify; text-align-last: left;
    color: var(--ink); font-size: 11.4px; line-height: 13.4px;
  }
  .panel { position: absolute; background: var(--panel-dark); }
  .panel.facts { left: 32px; top: 240px; width: 169px; height: 260px; }
  .panel.code { left: 233px; top: 372px; width: 119px; height: 125px; }
  .vertical-note {
    position: absolute; writing-mode: vertical-rl; transform: rotate(180deg);
    color: var(--ink);
  }
  .vertical-note.small {
    left: 203px; top: 253px; height: 226px;
    font-size: 8.6px; line-height: 10px; text-align: center;
  }
  .vertical-note.large {
    left: 238px; top: 250px; height: 112px;
    font-size: 12.4px; line-height: 11.6px; text-align: left;
  }
</style>
</head>
<body>
<main class="sheet">
  <section class="label label-front">
    <div class="flavor-initial">V</div>
    <div class="brand-square"></div>
    <div class="brand-name">
      <span class="primary">LARKMOOR</span>
      <span class="secondary">HOLLOW FARM</span>
    </div>
    <h1 class="product-name">RAW<br>HONEY</h1>
    <div class="rule product"></div>
    <p class="infusion">CBD OIL &amp; VANILLA</p>
    <p class="net-weight">NET WT 44OZ</p>
    <div class="rule weight"></div>
    <p class="front-copy">LOREM IPSUM DOLOR SIT AMET, CONSECTETUER ADIPISCING ELIT, SED DIAM NONUMMY NIBH EUISMOD TINCIDUNT UT LAOREET DOLORE MAGNA ALIQUAM ERAT VOLUTPAT. UT WISI ENIM AD MINIM VENIAM, QUIS NOSTRUD EXERCI TATION ULLAMCORPER</p>
  </section>

  <section class="label label-back">
    <div class="flavor-initial">V</div>
    <p class="back-copy">LOREM IPSUM DOLOR SIT AMET, CONSECTETUER ADIPISCING ELIT, SED DIAM NONUMMY NIBH EUISMOD TINCIDUNT UT LAOREET DOLORE MAGNA ALIQUAM ERAT VOLUTPAT. UT WISI ENIM AD MINIM VENIAM, QUIS NOSTRUD EXERCI TATION ULLAMCORPER EUISMOD TINCIDUNT UT LAOREET DOLORE MAGNA ALIQUAM ERAT VOLUTPAT. UT WISI ENIM AD MINIM VENIAM, QUIS NOSTRUD EXERCI TATION ULLAMCORPER. UT WISI ENIM AD MINIM VENIAM, QUIS.</p>
    <div class="panel facts"></div>
    <p class="vertical-note small">LOREM IPSUM DOLOR SIT AMET, CONSECTETUER<br>ADIPISCING ELIT, DIAM</p>
    <p class="vertical-note large">LOREM IPSUM<br>DOLOR SIT AMET,<br>CONSECTETUER<br>ADIPISCING ELIT,<br>DIAM NONUMMY<br>NIBH EUISMOD<br>TINCIDUNT UT<br>LAOREET DOLORE</p>
    <div class="panel code"></div>
  </section>
</main>
</body>
</html>
```